EPIC, awesome, creative business card needed - get involved!

I'm launching a boutique, exclusive Property Management real estate agency in Sydney early next year.
The name of the agency will be called "Quartz Hill Lane" - it's a play on "chase the silver pebble trail" to wealth. The Quartz Hill Lane signifies wealth through property investment.
My business will offer management of investment properties (ie Property Management).
The difference with Quartz Hill Lane and other agencies is the business will be run by one of Australia's leading property investment experts, and also one of Australia's leading property managers.
It will be exclusively for high net worth properties and individuals, so the business card needs to be extremely sharp, slick and relatively simple.
The information I want on the card is as follows
Nolan Pryce - Director
M: 0412 967 154
P: 9735 6021
E: nolan@quartzhilllane.net.au
W: quartzhilllane.net.au
I'm happy with the red from the logo, black - no yellows or funky colors. I want this to be a super corporate and slick business card to match the high end nature of the business.
Good luck everyone, and please ask questions for clarification.

```html
<!DOCTYPE html>
<html lang="en">
<head>
<meta charset="utf-8">
<title>Quartz Hill Lane – Business Card</title>
<link rel="stylesheet" href="https://fonts.googleapis.com/css2?family=Open+Sans:wght@400;700&display=swap">
<style>
  :root {
    --page: #ffffff;
    --card-front: #111111;
    --card-back: #404040;
    --tab-light: #3c3c3c;
    --tab-dark: #111111;
    --brand-red: #c00000;
    --ink: #ffffff;
  }
  * { margin: 0; padding: 0; box-sizing: border-box; }
  html, body {
    width: 1200px; height: 348px; overflow: hidden;
    background: var(--page);
    font-family: "Open Sans", sans-serif;
  }
  .canvas { position: relative; width: 1200px; height: 348px; }

  .card { position: absolute; top: 20px; width: 527px; height: 299px; overflow: hidden; }
  .card--front { left: 18px; background: var(--card-front); }
  .card--back { left: 617px; background: var(--card-back); }

  .tab { position: absolute; top: 23px; width: 26px; height: 254px; }
  .card--front .tab { background: var(--tab-light); }
  .card--back .tab { background: var(--tab-dark); }
  .tab--left { left: 0; border-radius: 0 16px 16px 0; }
  .tab--right { right: 0; border-radius: 16px 0 0 16px; }

  .brand { position: absolute; display: flex; color: var(--ink); font-weight: 700; text-transform: uppercase; }
  .brand__square { background: var(--brand-red); flex: none; }
  .brand__name { line-height: 1.05; letter-spacing: 0.5px; }

  .card--front .brand { left: 64px; top: 62px; flex-direction: column; gap: 14px; }
  .card--front .brand__square { width: 48px; height: 48px; }
  .card--front .brand__name { font-size: 36px; }

  .card--back .brand { left: 83px; top: 74px; align-items: center; gap: 26px; }
  .card--back .brand__square { width: 150px; height: 150px; }
  .card--back .brand__name { font-size: 44px; }

  .contact {
    position: absolute; left: 287px; top: 133px;
    color: var(--ink); font-size: 14px; line-height: 20px; list-style: none;
  }
  .contact__role { font-size: 11px; }
</style>
</head>
<body>
<main class="canvas">
  <section class="card card--front" aria-label="Card front">
    <div class="tab tab--left"></div>
    <div class="tab tab--right"></div>
    <div class="brand">
      <span class="brand__square"></span>
      <p class="brand__name">Quartz<br>Hill<br>Lane</p>
    </div>
    <ul class="contact">
      <li>Nolan Pryce - <span class="contact__role">Director</span></li>
      <li>M: 0412 967 154</li>
      <li>P: 9735 6021</li>
      <li>E: nolan@quartzhilllane.net.au</li>
      <li>W: quartzhilllane.net.au</li>
    </ul>
  </section>

  <section class="card card--back" aria-label="Card back">
    <div class="tab tab--left"></div>
    <div class="tab tab--right"></div>
    <div class="brand">
      <span class="brand__square"></span>
      <p class="brand__name">Quartz<br>Hill<br>Lane</p>
    </div>
  </section>
</main>
</body>
</html>
```